Social News web page design website name Vorlet.

I need a web design for a start up project called Vorlet based in Sydney. Its a social news website. it helps people to get centralized news and people can have their own profiles where they can post there thoughts and comments and it will be free to signup and usage as well.

I would like to see designs that use the latest pelican scaffold framework and are mobile compatible. only need 2 pages a home page kind of similar to
plonk (http://plonk.example/) and a profile that's a next gen user profile page I will leave that to you imaginations

this is my previous design I did on my own http://www.vorlet.example/

Target Market(s)

target market is 13 and up and anyone who likes or uses social media and would be able to understand the site

Industry/Entity Type

News

Requirements
Must have
• 1.) using pelican scaffold. 2) a home page similar to plonk (http://plonk.example/) or even better free to use your imagination 3) a next gen profile page better the one i made on my own which is this one (http://www.vorlet.example/profile/hollisbrackett) 4) for mobile navigation, have a mobile navigation something similar to http://slidepanel.quenrow.example/
Nice to have
• 1) a sexy navigation and layout for both desktop and mobile phones. i will leave that to you imaginations. 2) social medial buttons like to sign-in with and also to post a story to Chatterly or pelican 3) a user settings page (but not necessary) 4) a login or signup (but not necessary)

```html
<!DOCTYPE html>
<html lang="en">
<head>
<meta charset="utf-8">
<title>Vorlet – Social News</title>
<link href="https://fonts.googleapis.com/css2?family=Roboto:wght@300;400;500;700&display=swap" rel="stylesheet">
<style>
:root{
  --page:#f2f2f2;
  --white:#ffffff;
  --ink:#1d1d1d;
  --text:#333333;
  --muted:#777777;
  --line:#dcdcdc;
  --band:#000000;
  --footer:#141414;
  --share-1:#3b5998;
  --share-2:#2fa8e0;
  --share-3:#1f78b4;
  --share-4:#f08c1e;
}
*{box-sizing:border-box;margin:0;padding:0}
html,body{width:1200px;height:2956px;overflow:hidden}
body{font-family:"Roboto",Arial,sans-serif;background:var(--page);color:var(--text);position:relative}

/* header */
.site-header{position:absolute;top:0;left:0;width:1200px;height:44px;background:var(--white);border-bottom:1px solid var(--line)}
.brand{position:absolute;left:142px;top:9px;font-size:22px;font-weight:700;color:var(--ink);letter-spacing:.5px}
.main-nav{position:absolute;left:246px;top:14px;display:flex;gap:32px}
.main-nav a{font-size:13px;letter-spacing:1.5px;color:var(--ink);text-decoration:none;text-transform:uppercase}
.search{position:absolute;left:918px;top:11px;width:138px;height:22px;border:1px solid #c9c9c9;background:var(--white);font-size:10px;color:var(--muted);padding:5px 6px}
.search svg{position:absolute;right:4px;top:4px}

/* hero */
.hero{position:absolute;left:138px;top:55px;width:926px;height:335px}
.hero-photo{position:absolute;left:0;top:0;width:587px;height:335px;border:4px solid #d6d6d6;background:linear-gradient(160deg,#e8d6c8,#c9a08a 55%,#8a6a58)}
.hero-text{position:absolute;left:617px;top:28px;width:310px}
.hero-title{font-size:22px;font-weight:400;line-height:29px;color:var(--ink)}
.hero-date{font-size:11px;color:var(--muted);margin-top:6px}
.hero-lead{font-size:12px;line-height:20px;color:var(--muted);margin-top:18px}

/* story grid */
.story-grid{position:absolute;left:138px;top:406px;width:926px;display:grid;grid-template-columns:repeat(3,293px);column-gap:23.5px;row-gap:61px}
.story-card{height:286px;background:var(--white);border:1px solid var(--line);display:flex;flex-direction:column}
.story-photo{height:154px}
.story-body{padding:14px 8px 0;flex:1}
.story-title{font-size:12.5px;font-weight:500;line-height:18px;color:var(--ink)}
.story-desc{font-size:11.5px;line-height:19px;color:var(--muted);margin-top:6px}
.story-foot{height:34px;border-top:1px solid var(--line);display:flex;align-items:center;justify-content:space-between;padding:0 10px}
.vote{font-size:11.5px;color:var(--text)}
.share{display:flex;gap:3px}
.share i{display:block;width:14px;height:14px;border-radius:2px}
.s1{background:var(--share-1)}.s2{background:var(--share-2)}.s3{background:var(--share-3)}.s4{background:var(--share-4)}

/* videos */
.video-band{position:absolute;left:0;top:2128px;width:1200px;height:272px;background:var(--band)}
.band-title{position:absolute;left:138px;top:30px;font-size:13px;color:var(--white)}
.video-row{position:absolute;left:138px;top:65px;display:grid;grid-template-columns:repeat(4,214px);column-gap:23.5px}
.video-thumb{position:relative;height:120px}
.video-thumb svg{position:absolute;left:50%;top:50%;transform:translate(-50%,-50%)}
.video-title{font-size:12px;color:var(--white);margin-top:10px}
.video-desc{font-size:10.5px;line-height:15px;color:#8c8c8c;margin-top:4px}

/* lists */
.lists{position:absolute;left:0;top:2400px;width:1200px;height:496px;background:var(--page)}
.list-col{position:absolute;top:28px;width:420px}
.list-col.left{left:138px}
.list-col.right{left:644px}
.divider{position:absolute;left:601px;top:30px;width:1px;height:450px;background:var(--line)}
.list-head{font-size:17px;font-weight:400;color:var(--ink);margin-bottom:16px}
.list-item{position:relative;padding-left:42px;margin-bottom:13px}
.list-item svg{position:absolute;left:20px;top:4px}
.list-item h3{font-size:12.5px;font-weight:400;line-height:18px;color:var(--ink)}
.list-item p{font-size:9.5px;color:var(--muted);margin-top:2px;text-transform:uppercase}
.list-item p span{text-transform:none}

/* footer */
.site-footer{position:absolute;left:0;top:2896px;width:1200px;height:60px;background:var(--footer)}
.follow{position:absolute;left:144px;top:22px;display:flex;align-items:center;gap:4px;font-size:11.5px;color:#a0a0a0}
.follow span{margin-right:6px}
.follow i{display:block;width:14px;height:14px;border-radius:2px}
.footer-links{position:absolute;right:136px;top:23px;font-size:10px;color:#a0a0a0}
.footer-links a{color:#a0a0a0;text-decoration:none}
</style>
</head>
<body>

<header class="site-header">
  <div class="brand">Vorlet</div>
  <nav class="main-nav">
    <a href="#">Home</a><a href="#">Post</a><a href="#">Sign in</a><a href="#">Sign up</a>
  </nav>
  <div class="search">Search
    <svg width="12" height="12" viewBox="0 0 12 12"><circle cx="5" cy="5" r="3.5" fill="none" stroke="#777" stroke-width="1.3"/><line x1="7.6" y1="7.6" x2="11" y2="11" stroke="#777" stroke-width="1.4"/></svg>
  </div>
</header>

<section class="hero">
  <div class="hero-photo" role="img" aria-label="Portrait photo of the film director"></div>
  <div class="hero-text">
    <h1 class="hero-title">Film: Silver Lanterns: Ehrenpreis für Wilbur Fenn</h1>
    <p class="hero-date">Montag, 13.01.2014, 04:29</p>
    <p class="hero-lead">Fenn hat über 55 Filme gedreht, zuletzt war „Grey Harbour" mit Conrad Pell und Ines Varga in den Kinos.</p>
  </div>
</section>

<main class="story-grid">
  <article class="story-card"><div class="story-photo" role="img" aria-label="Football player injured on the field" style="background:linear-gradient(135deg,#1e2c4a,#7a2430 60%,#3b4a6a)"></div><div class="story-body"><h2 class="story-title">Darnell Okafor Injury: Updates on Harbor Hawks LB's Leg and Return</h2><p class="story-desc">Bayport Harbor Hawks linebacker Darnell Okafor suffered a scary injury in the NCC Championship Game against the Riverton</p></div><div class="story-foot"><span class="vote">Vote &nbsp;(0)</span><span class="share"><i class="s1"></i><i class="s2"></i><i class="s3"></i><i class="s4"></i></span></div></article>
  <article class="story-card"><div class="story-photo" role="img" aria-label="Graduates celebrating outdoors" style="background:linear-gradient(135deg,#5e86b8,#2b2b33 55%,#4f7a3e)"></div><div class="story-body"><h2 class="story-title">Darnell Okafor Injury: Updates on Harbor Hawks LB's Leg and Return</h2><p class="story-desc">Bayport Harbor Hawks linebacker Darnell Okafor suffered a scary injury in the NCC Championship Game against the Riverton</p></div><div class="story-foot"><span class="vote">Vote &nbsp;(0)</span><span class="share"><i class="s1"></i><i class="s2"></i><i class="s3"></i><i class="s4"></i></span></div></article>
  <article class="story-card"><div class="story-photo" role="img" aria-label="Illustration of a head in profile with a maze" style="background:linear-gradient(135deg,#d9a15a,#2f5f86 55%,#c58a45)"></div><div class="story-body"><h2 class="story-title">Darnell Okafor Injury: Updates on Harbor Hawks LB's Leg and Return</h2><p class="story-desc">Bayport Harbor Hawks linebacker Darnell Okafor suffered a scary injury in the NCC Championship Game against the Riverton</p></div><div class="story-foot"><span class="vote">Vote &nbsp;(0)</span><span class="share"><i class="s1"></i><i class="s2"></i><i class="s3"></i><i class="s4"></i></span></div></article>

  <article class="story-card"><div class="story-photo" role="img" aria-label="Dark stormy sci-fi landscape" style="background:linear-gradient(180deg,#3c4248,#55595c 50%,#2a2c2e)"></div><div class="story-body"><h2 class="story-title">Darnell Okafor Injury: Updates on Harbor Hawks LB's Leg and Return</h2><p class="story-desc">Bayport Harbor Hawks linebacker Darnell Okafor suffered a scary injury in the NCC Championship Game against the Riverton</p></div><div class="story-foot"><span class="vote">Vote &nbsp;(0)</span><span class="share"><i class="s1"></i><i class="s2"></i><i class="s3"></i><i class="s4"></i></span></div></article>
  <article class="story-card"><div class="story-photo" role="img" aria-label="Portrait photo of an actor" style="background:linear-gradient(90deg,#2a5fae,#c49a80 35%,#b3866c 65%,#9fc1e0)"></div><div class="story-body"><h2 class="story-title">Darnell Okafor Injury: Updates on Harbor Hawks LB's Leg and Return</h2><p class="story-desc">Bayport Harbor Hawks linebacker Darnell Okafor suffered a scary injury in the NCC Championship Game against the Riverton</p></div><div class="story-foot"><span class="vote">Vote &nbsp;(0)</span><span class="share"><i class="s1"></i><i class="s2"></i><i class="s3"></i><i class="s4"></i></span></div></article>
  <article class="story-card"><div class="story-photo" role="img" aria-label="Glowing nebula in deep space" style="background:radial-gradient(circle at 50% 50%,#fff4d6,#d8893c 22%,#3a2418 55%,#0d0a10)"></div><div class="story-body"><h2 class="story-title">Darnell Okafor Injury: Updates on Harbor Hawks LB's Leg and Return</h2><p class="story-desc">Bayport Harbor Hawks linebacker Darnell Okafor suffered a scary injury in the NCC Championship Game against the Riverton</p></div><div class="story-foot"><span class="vote">Vote &nbsp;(0)</span><span class="share"><i class="s1"></i><i class="s2"></i><i class="s3"></i><i class="s4"></i></span></div></article>

  <article class="story-card"><div class="story-photo" role="img" aria-label="Dark film still of a masked hero" style="background:linear-gradient(135deg,#050505,#2b2a28 55%,#0a0a0a)"></div><div class="story-body"><h2 class="story-title">Darnell Okafor Injury: Updates on Harbor Hawks LB's Leg and Return</h2><p class="story-desc">Bayport Harbor Hawks linebacker Darnell Okafor suffered a scary injury in the NCC Championship Game against the Riverton</p></div><div class="story-foot"><span class="vote">Vote &nbsp;(0)</span><span class="share"><i class="s1"></i><i class="s2"></i><i class="s3"></i><i class="s4"></i></span></div></article>
  <article class="story-card"><div class="story-photo" role="img" aria-label="Football players in action" style="background:linear-gradient(135deg,#c9ccc8,#2f4f3e 55%,#8d9290)"></div><div class="story-body"><h2 class="story-title">Darnell Okafor Injury: Updates on Harbor Hawks LB's Leg and Return</h2><p class="story-desc">Bayport Harbor Hawks linebacker Darnell Okafor suffered a scary injury in the NCC Championship Game against the Riverton</p></div><div class="story-foot"><span class="vote">Vote &nbsp;(0)</span><span class="share"><i class="s1"></i><i class="s2"></i><i class="s3"></i><i class="s4"></i></span></div></article>
  <article class="story-card"><div class="story-photo" role="img" aria-label="Excited crowd at an awards event" style="background:linear-gradient(135deg,#d8b39a,#8a3a2e 50%,#3a6a8a)"></div><div class="story-body"><h2 class="story-title">Darnell Okafor Injury: Updates on Harbor Hawks LB's Leg and Return</h2><p class="story-desc">Bayport Harbor Hawks linebacker Darnell Okafor suffered a scary injury in the NCC Championship Game against the Riverton</p></div><div class="story-foot"><span class="vote">Vote &nbsp;(0)</span><span class="share"><i class="s1"></i><i class="s2"></i><i class="s3"></i><i class="s4"></i></span></div></article>

  <article class="story-card"><div class="story-photo" role="img" aria-label="Stadium with broadcast stage" style="background:linear-gradient(180deg,#9aa6b4,#c8c4c0 40%,#9b2a2a 70%,#5a6f4a)"></div><div class="story-body"><h2 class="story-title">Darnell Okafor Injury: Updates on Harbor Hawks LB's Leg and Return</h2><p class="story-desc">Bayport Harbor Hawks linebacker Darnell Okafor suffered a scary injury in the NCC Championship Game against the Riverton</p></div><div class="story-foot"><span class="vote">Vote &nbsp;(0)</span><span class="share"><i class="s1"></i><i class="s2"></i><i class="s3"></i><i class="s4"></i></span></div></article>
  <article class="story-card"><div class="story-photo" role="img" aria-label="Aerial view of green land and a highway" style="background:linear-gradient(135deg,#8aa0b0,#5d7a4a 45%,#8c2f2f 85%)"></div><div class="story-body"><h2 class="story-title">Darnell Okafor Injury: Updates on Harbor Hawks LB's Leg and Return</h2><p class="story-desc">Bayport Harbor Hawks linebacker Darnell Okafor suffered a scary injury in the NCC Championship Game against the Riverton</p></div><div class="story-foot"><span class="vote">Vote &nbsp;(0)</span><span class="share"><i class="s1"></i><i class="s2"></i><i class="s3"></i><i class="s4"></i></span></div></article>
  <article class="story-card"><div class="story-photo" role="img" aria-label="Illustration of a head in profile with a maze" style="background:linear-gradient(135deg,#d9a15a,#2f5f86 55%,#c58a45)"></div><div class="story-body"><h2 class="story-title">Darnell Okafor Injury: Updates on Harbor Hawks LB's Leg and Return</h2><p class="story-desc">Bayport Harbor Hawks linebacker Darnell Okafor suffered a scary injury in the NCC Championship Game against the Riverton</p></div><div class="story-foot"><span class="vote">Vote &nbsp;(0)</span><span class="share"><i class="s1"></i><i class="s2"></i><i class="s3"></i><i class="s4"></i></span></div></article>

  <article class="story-card"><div class="story-photo" role="img" aria-label="Concert crowd under stage lights" style="background:linear-gradient(180deg,#f0c070,#8a4a1a 40%,#1a0e08)"></div><div class="story-body"><h2 class="story-title">Darnell Okafor Injury: Updates on Harbor Hawks LB's Leg and Return</h2><p class="story-desc">Bayport Harbor Hawks linebacker Darnell Okafor suffered a scary injury in the NCC Championship Game against the Riverton</p></div><div class="story-foot"><span class="vote">Vote &nbsp;(0)</span><span class="share"><i class="s1"></i><i class="s2"></i><i class="s3"></i><i class="s4"></i></span></div></article>
  <article class="story-card"><div class="story-photo" role="img" aria-label="Audience in a conference hall" style="background:linear-gradient(180deg,#3a2a20,#8a3a2a 50%,#2a1a14)"></div><div class="story-body"><h2 class="story-title">Darnell Okafor Injury: Updates on Harbor Hawks LB's Leg and Return</h2><p class="story-desc">Bayport Harbor Hawks linebacker Darnell Okafor suffered a scary injury in the NCC Championship Game against the Riverton</p></div><div class="story-foot"><span class="vote">Vote &nbsp;(0)</span><span class="share"><i class="s1"></i><i class="s2"></i><i class="s3"></i><i class="s4"></i></span></div></article>
  <article class="story-card"><div class="story-photo" role="img" aria-label="Tech expo floor in blue light" style="background:linear-gradient(135deg,#1a1e6a,#4a3ab0 50%,#12123a)"></div><div class="story-body"><h2 class="story-title">Darnell Okafor Injury: Updates</h2><p class="story-desc">Bayport Harbor Hawks linebacker Darnell Okafor suffered a scary injury in the NCC Championship Game against the Riverton</p></div><div class="story-foot"><span class="vote">Vote &nbsp;(0)</span><span class="share"><i class="s1"></i><i class="s2"></i><i class="s3"></i><i class="s4"></i></span></div></article>
</main>

<section class="video-band">
  <h2 class="band-title">Most Popular Videos</h2>
  <div class="video-row">
    <div class="video-item"><div class="video-thumb" role="img" aria-label="Football match video still" style="background:linear-gradient(135deg,#2a3a5a,#c8c8c8 50%,#8a2a2a)"><svg width="40" height="40" viewBox="0 0 40 40"><circle cx="20" cy="20" r="18" fill="none" stroke="#fff" stroke-width="3"/><polygon points="16,12 29,20 16,28" fill="#fff"/></svg></div><h3 class="video-title">Darnell Okafor Injury: Updates</h3><p class="video-desc">Bayport Harbor Hawks linebacker<br>Darnell Okafor suffered a scar</p></div>
    <div class="video-item"><div class="video-thumb" role="img" aria-label="Ice hockey video still" style="background:linear-gradient(135deg,#2a3a6a,#e0e4ea 50%,#a02a2a)"><svg width="40" height="40" viewBox="0 0 40 40"><circle cx="20" cy="20" r="18" fill="none" stroke="#fff" stroke-width="3"/><polygon points="16,12 29,20 16,28" fill="#fff"/></svg></div><h3 class="video-title">Darnell Okafor Injury: Updates</h3><p class="video-desc">Bayport Harbor Hawks linebacker<br>Darnell Okafor suffered a scar</p></div>
    <div class="video-item"><div class="video-thumb" role="img" aria-label="Football tackle video still" style="background:linear-gradient(135deg,#6a4a4a,#c0a090 50%,#3a2a3a)"><svg width="40" height="40" viewBox="0 0 40 40"><circle cx="20" cy="20" r="18" fill="none" stroke="#fff" stroke-width="3"/><polygon points="16,12 29,20 16,28" fill="#fff"/></svg></div><h3 class="video-title">Darnell Okafor Injury: Updates</h3><p class="video-desc">Bayport Harbor Hawks linebacker<br>Darnell Okafor suffered a scar</p></div>
    <div class="video-item"><div class="video-thumb" role="img" aria-label="Soccer match video still" style="background:linear-gradient(135deg,#3a5a9a,#c83a3a 50%,#3a8a3a)"><svg width="40" height="40" viewBox="0 0 40 40"><circle cx="20" cy="20" r="18" fill="none" stroke="#fff" stroke-width="3"/><polygon points="16,12 29,20 16,28" fill="#fff"/></svg></div><h3 class="video-title">Darnell Okafor Injury: Updates</h3><p class="video-desc">Bayport Harbor Hawks linebacker<br>Darnell Okafor suffered a scar</p></div>
  </div>
</section>

<section class="lists">
  <div class="list-col left">
    <h2 class="list-head">Internet Trends</h2>
    <div class="list-item"><svg width="10" height="10" viewBox="0 0 10 10"><path d="M1 1l4 4-4 4M5 1l4 4-4 4" fill="none" stroke="#555" stroke-width="1.2"/></svg><h3>More Problems for American Couple Accused in Veloria</h3><p>By Daniel Rourke and Meera T. Anand <span>JAN. 21, 2014</span></p></div>
    <div class="list-item"><svg width="10" height="10" viewBox="0 0 10 10"><path d="M1 1l4 4-4 4M5 1l4 4-4 4" fill="none" stroke="#555" stroke-width="1.2"/></svg><h3>Tomas Ferrer vs. Pavel Ristov: Recap and Results from<br>Southern Cross Open 2014</h3><p>By Daniel Rourke and Meera T. Anand <span>JAN. 21, 2014</span></p></div>
    <div class="list-item"><svg width="10" height="10" viewBox="0 0 10 10"><path d="M1 1l4 4-4 4M5 1l4 4-4 4" fill="none" stroke="#555" stroke-width="1.2"/></svg><h3>For Canadian Teenager, to Believe Is to Belong</h3><p>By Daniel Rourke and Meera T. Anand <span>JAN. 21, 2014</span></p></div>
    <div class="list-item"><svg width="10" height="10" viewBox="0 0 10 10"><path d="M1 1l4 4-4 4M5 1l4 4-4 4" fill="none" stroke="#555" stroke-width="1.2"/></svg><h3>Where would Marco Solen play ...</h3><p>By Daniel Rourke and Meera T. Anand <span>JAN. 21, 2014</span></p></div>
    <div class="list-item"><svg width="10" height="10" viewBox="0 0 10 10"><path d="M1 1l4 4-4 4M5 1l4 4-4 4" fill="none" stroke="#555" stroke-width="1.2"/></svg><h3>More Problems for American Couple Accused in Veloria</h3><p>By Daniel Rourke and Meera T. Anand <span>JAN. 21, 2014</span></p></div>
    <div class="list-item"><svg width="10" height="10" viewBox="0 0 10 10"><path d="M1 1l4 4-4 4M5 1l4 4-4 4" fill="none" stroke="#555" stroke-width="1.2"/></svg><h3>Tomas Ferrer vs. Pavel Ristov: Recap and Results from<br>Southern Cross Open 2014</h3><p>By Daniel Rourke and Meera T. Anand <span>JAN. 21, 2014</span></p></div>
    <div class="list-item"><svg width="10" height="10" viewBox="0 0 10 10"><path d="M1 1l4 4-4 4M5 1l4 4-4 4" fill="none" stroke="#555" stroke-width="1.2"/></svg><h3>For Canadian Teenager, to Believe Is to Belong</h3><p>By Daniel Rourke and Meera T. Anand <span>JAN. 21, 2014</span></p></div>
    <div class="list-item"><svg width="10" height="10" viewBox="0 0 10 10"><path d="M1 1l4 4-4 4M5 1l4 4-4 4" fill="none" stroke="#555" stroke-width="1.2"/></svg><h3>Where would Marco Solen play ...</h3><p>By Daniel Rourke and Meera T. Anand <span>JAN. 21, 2014</span></p></div>
  </div>
  <div class="divider"></div>
  <div class="list-col right">
    <h2 class="list-head">Popular Stories</h2>
    <div class="list-item"><svg width="10" height="10" viewBox="0 0 10 10"><path d="M1 1l4 4-4 4M5 1l4 4-4 4" fill="none" stroke="#555" stroke-width="1.2"/></svg><h3>More Problems for American Couple Accused in Veloria</h3><p>By Daniel Rourke and Meera T. Anand <span>JAN. 21, 2014</span></p></div>
    <div class="list-item"><svg width="10" height="10" viewBox="0 0 10 10"><path d="M1 1l4 4-4 4M5 1l4 4-4 4" fill="none" stroke="#555" stroke-width="1.2"/></svg><h3>Tomas Ferrer vs. Pavel Ristov: Recap and Results from<br>Southern Cross Open 2014</h3><p>By Daniel Rourke and Meera T. Anand <span>JAN. 21, 2014</span></p></div>
    <div class="list-item"><svg width="10" height="10" viewBox="0 0 10 10"><path d="M1 1l4 4-4 4M5 1l4 4-4 4" fill="none" stroke="#555" stroke-width="1.2"/></svg><h3>For Canadian Teenager, to Believe Is to Belong</h3><p>By Daniel Rourke and Meera T. Anand <span>JAN. 21, 2014</span></p></div>
    <div class="list-item"><svg width="10" height="10" viewBox="0 0 10 10"><path d="M1 1l4 4-4 4M5 1l4 4-4 4" fill="none" stroke="#555" stroke-width="1.2"/></svg><h3>Where would Marco Solen play ...</h3><p>By Daniel Rourke and Meera T. Anand <span>JAN. 21, 2014</span></p></div>
    <div class="list-item"><svg width="10" height="10" viewBox="0 0 10 10"><path d="M1 1l4 4-4 4M5 1l4 4-4 4" fill="none" stroke="#555" stroke-width="1.2"/></svg><h3>More Problems for American Couple Accused in Veloria</h3><p>By Daniel Rourke and Meera T. Anand <span>JAN. 21, 2014</span></p></div>
    <div class="list-item"><svg width="10" height="10" viewBox="0 0 10 10"><path d="M1 1l4 4-4 4M5 1l4 4-4 4" fill="none" stroke="#555" stroke-width="1.2"/></svg><h3>Tomas Ferrer vs. Pavel Ristov: Recap and Results from<br>Southern Cross Open 2014</h3><p>By Daniel Rourke and Meera T. Anand <span>JAN. 21, 2014</span></p></div>
    <div class="list-item"><svg width="10" height="10" viewBox="0 0 10 10"><path d="M1 1l4 4-4 4M5 1l4 4-4 4" fill="none" stroke="#555" stroke-width="1.2"/></svg><h3>For Canadian Teenager, to Believe Is to Belong</h3><p>By Daniel Rourke and Meera T. Anand <span>JAN. 21, 2014</span></p></div>
    <div class="list-item"><svg width="10" height="10" viewBox="0 0 10 10"><path d="M1 1l4 4-4 4M5 1l4 4-4 4" fill="none" stroke="#555" stroke-width="1.2"/></svg><h3>Where would Marco Solen play ...</h3><p>By Daniel Rourke and Meera T. Anand <span>JAN. 21, 2014</span></p></div>
  </div>
</section>

<footer class="site-footer">
  <div class="follow"><span>Follow us on</span><i class="s1"></i><i class="s2"></i><i class="s3"></i><i class="s4"></i></div>
  <div class="footer-links"><a href="#">Home</a> \ <a href="#">About Us</a> | <a href="#">News</a> | <a href="#">Blog</a> | <a href="#">Contact Us</a> | Copyrights @ 2014 All Rights Reserved</div>
</footer>

</body>
</html>
```